Website Q48 coffee

I am opening a small business selling locally roasted coffee online. To start with I want a site with three pages. 1. A welcome page with logo and mission/vision. 2. Shopping/ordering page. 3. About Us page. The brand is "Q48 Coffee - Brewed with bright hearts". We are giving back to the downs syndrome community by employing people with down syndrome (Trisomy 21) and buy donating to down syndrome research.

Target Market(s)

Families and friends of people with downs syndrome

Coding

Coded - Design and coding required

Number of Pages Required

3 page

```html
<!DOCTYPE html>
<html lang="en">
<head>
<meta charset="utf-8">
<title>Q48 Coffee - Brewed with bright hearts</title>
<link rel="stylesheet" href="https://fonts.googleapis.com/css2?family=IBM+Plex+Sans:wght@300;400;500;600;700&display=swap">
<style>
:root{
  --espresso:#1f0d03;
  --ink:#111111;
  --text:#333333;
  --white:#ffffff;
  --footer:#000000;
  --rule:#2a2a2a;
  --field:#8a8a8a;
  --badge:#ff5a2a;
}
*{box-sizing:border-box;margin:0;padding:0}
html,body{width:760px;height:1200px;overflow:hidden}
body{position:relative;background:var(--white);font-family:"IBM Plex Sans",Arial,sans-serif;color:var(--text)}
a{color:inherit;text-decoration:none}
.abs{position:absolute}

.promo-bar{left:0;top:0;width:760px;height:27px;background:var(--espresso);color:var(--white);font-size:9px;font-weight:600;display:flex;align-items:center;justify-content:center;gap:4px;letter-spacing:.2px}

.site-header{left:0;top:27px;width:760px;height:45px;background:var(--white)}
.brand{left:71px;top:8px;font-size:20px;font-weight:300;color:var(--ink);letter-spacing:1px;line-height:28px}
.main-nav{top:0;height:45px;font-size:10px;font-weight:500;color:var(--ink);letter-spacing:.3px}
.main-nav span{position:absolute;top:16px;white-space:nowrap;color:var(--ink)}
.header-icon{top:14px}
.cart-count{left:683px;top:13px;width:7px;height:7px;border-radius:50%;background:var(--badge);color:var(--white);font-size:5px;line-height:7px;text-align:center}

.hero{left:0;top:72px;width:760px;height:380px}
.hero-photo{left:0;top:0;width:760px;height:380px;background:linear-gradient(100deg,#1c0c04 0%,#2e170a 35%,#4e2c15 65%,#3a2010 100%)}
.hero-title{left:81px;top:131px;font-size:37px;font-weight:700;color:var(--white);letter-spacing:.5px;line-height:44px}
.hero-sub{left:82px;top:180px;font-size:20px;font-weight:500;color:var(--white);line-height:26px}
.hero-btn{left:81px;top:233px;width:106px;height:31px;border:1.5px solid var(--white);border-radius:16px;color:var(--white);font-size:10px;font-weight:600;display:flex;align-items:center;justify-content:center}
.hero-arrow{top:186px}
.slider-dots{left:352px;top:357px;display:flex;gap:7px}
.slider-dots i{width:7px;height:7px;border-radius:50%;background:rgba(255,255,255,.35)}
.slider-dots i.active{background:var(--white)}

.values-photo{left:72px;top:503px;width:291px;height:266px;background:linear-gradient(135deg,#efece5 0%,#d9d3c7 45%,#c9a45c 75%,#e3c040 100%)}
.value-icon{left:401px}
.value-title{left:401px;font-size:20px;font-weight:700;color:var(--ink);letter-spacing:.5px;line-height:22px}
.value-text{left:401px;font-size:8.8px;line-height:17px;color:var(--text)}

.signup{left:0;top:818px;width:760px;height:156px;background:radial-gradient(ellipse at 20% 60%,#3c2212 0%,#24120a 55%,#1a0c05 100%)}
.signup-title{left:0;top:30px;width:760px;text-align:center;font-size:24px;font-weight:700;color:var(--white);letter-spacing:.3px;line-height:30px}
.signup-sub{left:0;top:63px;width:760px;text-align:center;font-size:13.5px;color:var(--white);line-height:20px}
.signup-form{left:198px;top:93px;width:365px;height:29px;background:var(--white);display:flex}
.signup-field{flex:1;font-size:8.5px;color:var(--field);padding-left:14px;display:flex;align-items:center}
.signup-btn{width:82px;margin:1.5px;background:var(--espresso);color:var(--white);font-size:9.5px;font-weight:600;letter-spacing:.4px;display:flex;align-items:center;justify-content:center}

.site-footer{left:0;top:974px;width:760px;height:226px;background:var(--footer);color:var(--white)}
.footer-brand{left:71px;top:48px;font-size:30px;font-weight:300;letter-spacing:1.5px;line-height:36px}
.contact-line{left:74px;font-size:10px;display:flex;align-items:center;gap:5px;line-height:12px}
.footer-col{top:50px}
.footer-col h4{font-size:13px;font-weight:600;line-height:16px;margin-bottom:7px}
.footer-col li{list-style:none;font-size:9.8px;line-height:18.5px}
.footer-rule{left:0;top:192px;width:760px;height:1px;background:var(--rule)}
.copyright{left:71px;top:203px;font-size:9.8px;line-height:12px}
.pay-cards{left:478px;top:203px;display:flex;gap:5px}
.pay-cards i{width:18px;height:12px;border-radius:1.5px;background:#e6e6e6}
</style>
</head>
<body>

<div class="abs promo-bar">
  <svg width="10" height="8" viewBox="0 0 10 8" aria-hidden="true"><rect x="0" y="1" width="6" height="5" fill="#fff"/><path d="M6 3h2.5L10 5v1H6z" fill="#fff"/><circle cx="2" cy="7" r="1" fill="#fff"/><circle cx="8" cy="7" r="1" fill="#fff"/></svg>
  FREE SHIPPING ON ALL ORDERS
</div>

<header class="abs site-header">
  <div class="abs brand">Q48 Coffee</div>
  <nav class="abs main-nav" style="left:0;width:760px">
    <span style="left:409px">HOME</span>
    <span style="left:460px">|</span>
    <span style="left:486px">SHOPPING</span>
    <span style="left:560px">|</span>
    <span style="left:586px">ABOUT US</span>
  </nav>
  <svg class="abs header-icon" style="left:655px" width="13" height="13" viewBox="0 0 13 13" aria-label="Search"><circle cx="5.5" cy="5.5" r="4.5" fill="none" stroke="#111" stroke-width="1"/><path d="M9 9l3.5 3.5" stroke="#111" stroke-width="1"/></svg>
  <svg class="abs header-icon" style="left:674px" width="14" height="13" viewBox="0 0 14 13" aria-label="Cart"><path d="M0.5 1h2l2 7h7l1.5-5H3.5" fill="none" stroke="#111" stroke-width="1"/><circle cx="5.5" cy="11" r="1" fill="none" stroke="#111" stroke-width=".8"/><circle cx="10.5" cy="11" r="1" fill="none" stroke="#111" stroke-width=".8"/></svg>
  <div class="abs cart-count">0</div>
</header>

<section class="abs hero">
  <div class="abs hero-photo" role="img" aria-label="Cup of coffee with heart-shaped steam beside roasted coffee beans on burlap"></div>
  <h1 class="abs hero-title">Q48 COFFEE</h1>
  <p class="abs hero-sub">Brewed with bright hearts</p>
  <a class="abs hero-btn" href="#">SHOP NOW</a>
  <svg class="abs hero-arrow" style="left:44px" width="12" height="22" viewBox="0 0 12 22" aria-label="Previous slide"><path d="M11 1L1 11l10 10" fill="none" stroke="#fff" stroke-width="1.2"/></svg>
  <svg class="abs hero-arrow" style="left:701px" width="12" height="22" viewBox="0 0 12 22" aria-label="Next slide"><path d="M1 1l10 10L1 21" fill="none" stroke="#fff" stroke-width="1.2"/></svg>
  <div class="abs slider-dots"><i></i><i class="active"></i><i></i></div>
</section>

<div class="abs values-photo" role="img" aria-label="Two friends toasting with coffee mugs at a kitchen table"></div>

<svg class="abs value-icon" style="top:516px" width="42" height="22" viewBox="0 0 42 22" aria-hidden="true"><path d="M1 11C8 2 34 2 41 11C34 20 8 20 1 11Z" fill="none" stroke="#1f0d03" stroke-width="1.4"/><circle cx="21" cy="11" r="6.5" fill="none" stroke="#1f0d03" stroke-width="1.4"/><circle cx="21" cy="11" r="3" fill="none" stroke="#1f0d03" stroke-width="1.4"/></svg>
<h2 class="abs value-title" style="top:542px">OUR VISION</h2>
<p class="abs value-text" style="top:565px;width:282px">Develop A Company That Marketas Coffee And Related Products To Family And Friends Of The Down Syndrome Community</p>

<svg class="abs value-icon" style="top:613px" width="38" height="38" viewBox="0 0 38 38" aria-hidden="true"><circle cx="18" cy="20" r="16.5" fill="none" stroke="#1f0d03" stroke-width="1.4"/><circle cx="18" cy="20" r="11.5" fill="none" stroke="#1f0d03" stroke-width="1.4"/><circle cx="18" cy="20" r="6.5" fill="none" stroke="#1f0d03" stroke-width="1.4"/><circle cx="18" cy="20" r="2" fill="#1f0d03"/><path d="M18 20L33 5" stroke="#1f0d03" stroke-width="1.4"/><path d="M29 3l6-2-2 6z" fill="#1f0d03"/></svg>
<h2 class="abs value-title" style="top:656px">OUR MISSION</h2>
<p class="abs value-text" style="top:679px;width:296px">create and grow an online company selling contract roasted coffee. as growth permits become a fully vertically integrated coffee company from roasting to our own coffee shop. The company will give significant funds to medical research in downs syndrome and we will hire as many people with Downs syndrome as possible.</p>

<section class="abs signup">
  <h2 class="abs signup-title">SIGN UP &amp; SAVE</h2>
  <p class="abs signup-sub">Lorem ipsum dolor sit amet, consectetur adipiscing elit, sed do</p>
  <form class="abs signup-form">
    <div class="signup-field">Email Address</div>
    <div class="signup-btn">SUBSCRIBE</div>
  </form>
</section>

<footer class="abs site-footer">
  <div class="abs footer-brand">Q48 Coffee</div>
  <div class="abs contact-line" style="top:114px">
    <svg width="8" height="8" viewBox="0 0 8 8" aria-hidden="true"><path d="M1 0.5l1.5 0 1 2-1 1c.5 1 1 1.5 2 2l1-1 2 1V7.5C4 7.5.5 4 .5 1z" fill="#fff"/></svg>555 014 2748</div>
  <div class="abs contact-line" style="top:132px">
    <svg width="7" height="9" viewBox="0 0 7 9" aria-hidden="true"><path d="M3.5 9C1 5.5 0 4.5 0 3.3A3.5 3.5 0 0 1 7 3.3C7 4.5 6 5.5 3.5 9z" fill="#fff"/><circle cx="3.5" cy="3.3" r="1.2" fill="#000"/></svg>48 Roastery Lane Brightville USA 30148</div>
  <div class="abs contact-line" style="top:154px">
    <svg width="10" height="8" viewBox="0 0 10 8" aria-hidden="true"><rect x=".5" y=".5" width="9" height="7" fill="none" stroke="#fff"/><path d="M.5 .8L5 4.5 9.5 .8" fill="none" stroke="#fff"/></svg>hello@Q48Coffee.com</div>

  <div class="abs footer-col" style="left:342px">
    <h4>Quick Link</h4>
    <ul><li>Home</li><li>Shopping</li><li>About Us</li><li>Contact</li></ul>
  </div>
  <div class="abs footer-col" style="left:481px">
    <h4>Information</h4>
    <ul><li>Login</li><li>My Account</li><li>Terms &amp; Conditions</li><li>Order Tracking</li><li>Payment System</li><li>Promotional Offers</li></ul>
  </div>
  <div class="abs footer-col" style="left:637px">
    <h4>Follow us</h4>
    <ul><li>Friendhub</li><li>Chirper</li><li>Snapgram</li><li>Workline</li><li>Circle Plus</li><li>Viewtube</li></ul>
  </div>

  <div class="abs footer-rule"></div>
  <p class="abs copyright">© 2021 Q48 Coffee. All Rights Reserved.</p>
  <div class="abs pay-cards" role="img" aria-label="Accepted payment methods">
    <i></i><i style="background:#f2a13a"></i><i style="background:#f3d36a"></i><i style="background:#3a8fd0"></i><i style="background:#1e5aa8"></i><i style="background:#8a5ad0"></i><i style="background:#3a6ee0"></i><i style="background:#e8eef5"></i><i style="background:#b03ab0"></i>
  </div>
</footer>

</body>
</html>
```